Tallow Crest Partners Inc. - Marketing Materials (inserts for folder or electronic attachement)

I’m looking for 1-2 one page marketing pieces that will help market the services of Tallow Crest Partners Inc. (TCP). This is not a flyer per se. Rather something that I see as being used in a folder for prospective clients (even existing clients), “leave-behinds”, direct mail or emails to introduce them to the services of TCP and why they should choose our shop over the many others out there. I would like the marketing pieces to be adaptable over time, so that as the business environment changes, content in the pieces can be updated.
A little more about Tallow Crest Partners Inc.: TCP is an Alberta (Edmonton area) based Group Benefits Advisory/Consulting firm with a national reach. We are a boutique consulting shop specializing in Group Benefits. The principal (Derek Halvorsen) has been in the industry for 20 years and founded Tallow Crest Partners Inc., with the intent of providing clients "a different type of advisor/broker experience" and giving clients in the Alberta and the Canadian marketplace a better option. Leveraging experience and relationships, TCP's Value Proposition is to provide clients with expert and unbiased advice that will help implement the best program for their specific needs, all while ensuring maximum value. We provide customers a customized experience (no “one size fits all”) and a personalized service model. We focus in the Group Benefits arena (Extended Health Care, Dental Life and Disability, Health Care Spending Accounts, etc.), and use experts for other areas of insurance (Group RRSP and Individual Life insurance).

Key words and phrases to consider:
- cost vs. value,
- core values (transparency, integrity, honesty)
- impartial/unbiased advice
- fair
- we listen
- every customer is important
- personalized service model
- boutique advice, boutique services
- services that we offer/areas of speciality
- Deal with all major Insurers

Key requirements:

- ‘Professional’ feel to design. It is insurance related, after all.
- In keeping with the company name, the design should be modern.
- Blues, greys, teals and blacks are colours that are important and part of TCP’s existing logo.
- Graphics and/or pictures are acceptable.
- Key words: adaptable, expertise, honest(y), transparent, dependable, boutique, consulting, advice/advisory, value, customized approach, etc.

Ideally, this project would be something that could easily be scalable into other pieces and transition into letterhead/stationary as well.

Thank you.

Target Market(s)

Employers, HR Professionals, C suite execs and business owners with or looking for group benefits (employer sponsored Extended Health Care, Dental, Life and Disability) advice and representation.

Industry/Entity Type

Insurance Broker

Font styles to use
Sans Serif

Colors
33a6d7
85cae6
33b8a4
9d9d9d
5c5c5c
000000
86cfc6
3176b5

Requirements
Must have
• It must convey an air of Trust, Integrity, and of course, be modern looking and "fun". Insurance can be a stuffy field and I'd like to take some of the stuffiness away while maintaining a professional image. Also, this piece should be quickly recognizable and assimilated. That is, it should have information, but also be able to processed quickly.
Nice to have
• Have some "pop". Excite the reader and leave them wanting more.
• Flow charts, diagrams.
Should not have
• It must not be stuffy

```html
<!DOCTYPE html>
<html lang="en">
<head>
<meta charset="utf-8">
<title>Tallow Crest Partners – Benefit Advice</title>
<link rel="stylesheet" href="https://fonts.googleapis.com/css2?family=Montserrat:wght@500;600;700;800&family=Source+Sans+3:wght@400;600&display=swap">
<style>
  :root{
    --ink-dark:#2c5868;
    --teal:#74b3ab;
    --teal-light:#86cfc6;
    --teal-text:#5eaea4;
    --brand-teal:#33b8a4;
    --brand-blue:#3176b5;
    --body:#333b40;
    --white:#ffffff;
  }
  *{margin:0;padding:0;box-sizing:border-box}
  html,body{width:855px;height:1200px;overflow:hidden;background:var(--white)}
  .sheet{position:relative;width:855px;height:1200px;overflow:hidden;background:var(--white);font-family:"Source Sans 3",sans-serif;color:var(--body)}
  .abs{position:absolute}
  .photo{position:absolute;left:0;top:0}
  .brand{position:absolute;left:62px;top:112px;display:flex;align-items:center;gap:14px}
  .brand-dot{width:70px;height:70px;border-radius:50%;border:10px solid var(--brand-teal)}
  .brand-name{font-family:"Montserrat",sans-serif;font-weight:700;font-size:30px;line-height:1.05;color:var(--brand-teal);width:240px}
  .headline{position:absolute;font-family:"Montserrat",sans-serif;font-weight:800;font-size:36px;line-height:60px;padding:0 12px;white-space:nowrap}
  .headline-top{left:65px;top:304px;width:395px;height:61px;background:var(--ink-dark);color:var(--teal)}
  .headline-bottom{left:173px;top:365px;width:378px;height:60px;background:var(--teal);color:var(--ink-dark);padding-left:16px}
  .section-title{position:absolute;font-family:"Montserrat",sans-serif;font-weight:800;font-size:23px;color:var(--ink-dark)}
  .section-text{position:absolute;font-size:12.4px;line-height:19.6px;text-align:justify;text-align-last:left}
  .why-title{left:66px;top:648px}
  .why-text{left:66px;top:681px;width:296px}
  .who-title{left:495px;top:648px}
  .who-text{left:495px;top:681px;width:328px;color:var(--ink-dark)}
  .who-text strong{font-weight:600}
  .services-label{position:absolute;left:78px;top:820px;font-family:"Montserrat",sans-serif;font-weight:800;font-size:21px;color:var(--ink-dark)}
  .service{position:absolute;top:960px;width:240px;text-align:center}
  .service-title{font-family:"Montserrat",sans-serif;font-weight:700;font-size:18.5px;letter-spacing:3px;color:var(--teal-text);margin-bottom:8px}
  .service-text{font-size:12.2px;line-height:19.5px;color:var(--body)}
  .service-1{left:38px}
  .service-2{left:305px}
  .service-3{left:584px}
  .contact-label{position:absolute;left:94px;top:1105px;font-family:"Montserrat",sans-serif;font-weight:800;font-size:16px;letter-spacing:2.5px;color:var(--white)}
  .phone{position:absolute;left:440px;top:1120px;font-family:"Montserrat",sans-serif;font-weight:800;font-size:19px;color:var(--ink-dark)}
  .web{position:absolute;left:656px;top:1117px;font-size:12px;line-height:16px;color:var(--ink-dark);letter-spacing:.3px}
</style>
</head>
<body>
<div class="sheet">

  <svg class="photo" width="855" height="1200" viewBox="0 0 855 1200" role="img" aria-label="Photo of a desk seen from above with hands, laptop, coffee cup and financial papers">
    <defs>
      <linearGradient id="deskTone" x1="0" y1="0" x2="1" y2="1">
        <stop offset="0" stop-color="#3d3a37"/>
        <stop offset=".5" stop-color="#4a3f38"/>
        <stop offset="1" stop-color="#2f3436"/>
      </linearGradient>
    </defs>
    <polygon points="0,0 644,0 214,458 0,458" fill="url(#deskTone)"/>
  </svg>

  <svg class="photo" width="855" height="1200" viewBox="0 0 855 1200" role="img" aria-label="Photo of a young man in glasses and a denim shirt writing in a notebook on an orange seat">
    <defs>
      <linearGradient id="manTone" x1="0" y1="0" x2="1" y2="1">
        <stop offset="0" stop-color="#3d4e58"/>
        <stop offset=".45" stop-color="#506f8f"/>
        <stop offset=".75" stop-color="#c0713a"/>
        <stop offset="1" stop-color="#5e7696"/>
      </linearGradient>
    </defs>
    <polygon points="524,172 855,172 855,628 66,628" fill="url(#manTone)"/>
  </svg>

  <div class="brand">
    <div class="brand-dot"></div>
    <div class="brand-name">Tallow Crest Partners</div>
  </div>

  <div class="headline headline-top">Your Trusted Source</div>
  <div class="headline headline-bottom">For Benefit Advice</div>

  <svg class="abs" style="left:0;top:0" width="855" height="1200" viewBox="0 0 855 1200" aria-hidden="true">
    <polygon class="who-panel" points="326,630 855,630 855,802 496,802" fill="var(--teal)"/>
    <polygon class="who-band" points="614,802 855,802 855,838 652,838" fill="var(--ink-dark)"/>
    <polygon class="services-bar" points="65,816 345,816 378,849 65,849" fill="var(--teal)"/>
    <line class="services-line" x1="158" y1="914" x2="712" y2="914" stroke="var(--ink-dark)" stroke-width="2"/>
    <polygon class="contact-bar" points="65,1100 246,1100 279,1133 65,1133" fill="var(--ink-dark)"/>
    <polygon class="foot-band" points="316,1174 855,1174 855,1200 290,1200" fill="var(--teal)"/>

    <!-- service icons -->
    <g class="icon-health" transform="translate(158,914)">
      <polygon points="0,-34 30,-17 30,17 0,34 -30,17 -30,-17" fill="var(--ink-dark)"/>
      <path d="M0,15 C-24,-2 -20,-18 -9,-18 C-4,-18 -1,-15 0,-12 C1,-15 4,-18 9,-18 C20,-18 24,-2 0,15Z" fill="none" stroke="#fff" stroke-width="3"/>
      <polyline points="-16,-2 -7,-2 -3,-9 2,6 6,-2 16,-2" fill="none" stroke="#fff" stroke-width="2.2"/>
    </g>
    <g class="icon-ready" transform="translate(425,914)">
      <polygon points="0,-34 30,-17 30,17 0,34 -30,17 -30,-17" fill="var(--ink-dark)"/>
      <path d="M-14,-18 V-4 C-14,8 2,8 2,-4 V-18" fill="none" stroke="#fff" stroke-width="2.6"/>
      <path d="M-6,6 V12 C-6,20 12,20 12,10 V4" fill="none" stroke="#fff" stroke-width="2.6"/>
      <circle cx="12" cy="0" r="4.5" fill="none" stroke="#fff" stroke-width="2.4"/>
    </g>
    <g class="icon-else" transform="translate(712,914)">
      <polygon points="0,-34 30,-17 30,17 0,34 -30,17 -30,-17" fill="var(--ink-dark)"/>
      <path d="M8,-14 H-15 V16 H15 V2" fill="none" stroke="#fff" stroke-width="3"/>
      <polyline points="-8,-1 0,8 18,-16" fill="none" stroke="#fff" stroke-width="4"/>
    </g>

    <!-- contact icons -->
    <g class="icon-phone" transform="translate(414,1134)">
      <circle r="15" fill="var(--ink-dark)"/>
      <path d="M-8,-3 C-8,-8 8,-8 8,-3 L6,-1 L3,-3 L-3,-3 L-6,-1Z" fill="#fff"/>
      <rect x="-6" y="0" width="12" height="7" rx="1.5" fill="#fff"/>
    </g>
    <g class="icon-web" transform="translate(631,1134)">
      <circle r="15" fill="var(--ink-dark)"/>
      <circle r="9" fill="none" stroke="#fff" stroke-width="1.4"/>
      <ellipse rx="4" ry="9" fill="none" stroke="#fff" stroke-width="1.2"/>
      <line x1="-9" y1="0" x2="9" y2="0" stroke="#fff" stroke-width="1.2"/>
      <line x1="-8" y1="-4.5" x2="8" y2="-4.5" stroke="#fff" stroke-width="1"/>
      <line x1="-8" y1="4.5" x2="8" y2="4.5" stroke="#fff" stroke-width="1"/>
    </g>
  </svg>

  <h2 class="section-title why-title">Why Choose Us?</h2>
  <p class="section-text why-text">Your business is unique. Your employees are unique. Shouldn't your employee benefits program be designed with that in mind? Your group benefits program should reflect your organization's unique character and offer lasting value to you and your employees.</p>

  <h2 class="section-title who-title">Who We Are?</h2>
  <p class="section-text who-text"><strong>Integrity, Transparency, Customer Service and Empowerment</strong> are the pillars on which TCP was founded. Our mission is quite simple; to be your trusted advisor in the group insurance arena by ensuring the lasting value of your employee benefits investment.</p>

  <h2 class="services-label">Our&nbsp; Services</h2>

  <div class="service service-1">
    <h3 class="service-title">The Essentials</h3>
    <p class="service-text">Group Health and Dental plans.<br>Taylored to your needs. A different type<br>of advisor/broker experience.</p>
  </div>
  <div class="service service-2">
    <h3 class="service-title">Always Ready</h3>
    <p class="service-text">Life, Critical Illness and Income replacement.<br>We'll identify your needs and offer you the<br>best advise, always.</p>
  </div>
  <div class="service service-3">
    <h3 class="service-title">Everything Else</h3>
    <p class="service-text">Health, Wellness and cost plus.<br>Group RRSP, Life Insurance and<br>Estate planning.</p>
  </div>

  <div class="contact-label">CONTACT US</div>
  <div class="phone">+780-555-0148</div>
  <div class="web">www.tallowcrestpartners.com<br>info@tallowcrestpartners.ca</div>

</div>
</body>
</html>
```